3 page designs for our Travel Company!!

Hi there!
We need 3 page designs to add to our travel website. We have include the PSD files of relevant web pages for you to use. We would like the new designs to fit in with the pages we already have designed please (colours, layout & style)
We require the following pages:
1. Hotel Search Page
2. Hotel Page
- For these pages, we are looking for an aesthetic design layout that fits in line with the layout of the pages we have designed. (PSD files 'Tour Page' & 'Tour Search Pages')
- We want to see imaginative ways of arranging the content in pleasant and 'easy to read' layouts.
3. Mobile View Page
- This is simply the design layout for the 'Mobile View'.
- We want you to illustrate how the drop down menus will work.
- Simplicity is key here. We want the menus to be easy to understand
- The 'Discover Cayman' menu is the only menu with multiple sub categories (You can see this in the PSD file named 'Drop Down Menu')
You can find our support documents here at https://www.filquarry.net/sh/7k21mdqzhrtt93p/QWxeLmPNvKrtaZu8fGh02bYRq?dl=0
Please feel free to get imaginative with unique ways these pages can be played out!
Thank you!

```html
<!DOCTYPE html>
<html lang="en">
<head>
<meta charset="utf-8">
<title>IsleRoute – Hotel Search</title>
<link href="https://fonts.googleapis.com/css2?family=Montserrat:wght@400;500;600;700&family=Raleway:wght@400;500;600&family=Roboto+Condensed:wght@400&display=swap" rel="stylesheet">
<style>
  :root{
    --blue-dark:#0756a6;
    --blue-btn:#0c62c9;
    --blue-bright:#1a96d4;
    --green:#7cbd2c;
    --green-badge:#2fc07a;
    --page:#f4f5f7;
    --white:#ffffff;
    --ink:#1f1f1f;
    --text:#444a52;
    --muted:#9aa0a6;
    --line:#dcdfe3;
    --star:#f7b500;
    --star-off:#cfd3d7;
    --map-sea:#cfe6fb;
  }
  *{box-sizing:border-box;margin:0;padding:0}
  html,body{width:814px;height:1200px;overflow:hidden}
  body{position:relative;background:var(--page);font-family:'Raleway',sans-serif;color:var(--text)}
  .abs{position:absolute}

  /* header */
  .site-header{position:absolute;left:0;top:0;width:814px;height:76px;background:var(--white)}
  .brand{position:absolute;left:48px;top:25px;display:flex;align-items:center;gap:6px}
  .brand-mark{width:20px;height:20px;background:var(--green);border-radius:3px}
  .brand-name{font-family:'Montserrat',sans-serif;font-weight:700;font-size:23px;color:var(--blue-bright);letter-spacing:.2px}
  .top-nav{position:absolute;right:82px;top:33px;display:flex;gap:13px;font-family:'Montserrat',sans-serif;font-size:13px;letter-spacing:1px;color:#333}
  .user-icon{position:absolute;left:749px;top:28px}

  .main-nav{position:absolute;left:0;top:80px;width:814px;height:48px;background:var(--blue-dark);border-bottom:3px solid var(--green)}
  .main-nav ul{list-style:none;display:flex;gap:24px;position:absolute;left:48px;top:15px;font-family:'Montserrat',sans-serif;font-size:13px;font-weight:500;color:var(--white);letter-spacing:1px}

  /* search bar */
  .field{position:absolute;top:150px;width:131px;height:34px;background:var(--white);border:1.5px solid #e1e4e8;border-radius:3px;font-size:11px;color:var(--muted);padding:0 0 0 20px;line-height:31px;font-family:'Montserrat',sans-serif}
  .field svg{position:absolute;right:10px;top:8px}
  .search-btn{position:absolute;left:617px;top:150px;width:131px;height:34px;background:var(--blue-bright);border-radius:3px;color:var(--white);font-family:'Montserrat',sans-serif;font-size:12px;letter-spacing:1px;font-weight:500;text-align:center;line-height:34px}

  .results-bar{position:absolute;left:234px;top:206px;font-family:'Montserrat',sans-serif;font-size:11px;color:#555}
  .taxes{position:absolute;left:430px;top:206px;font-family:'Montserrat',sans-serif;font-size:11px;color:var(--green)}
  .sort-label{position:absolute;left:635px;top:206px;font-size:7.5px;font-family:'Montserrat',sans-serif;color:#666}
  .sort-select{position:absolute;left:672px;top:204px;width:76px;height:17px;background:var(--white);border:1px solid #e1e4e8;border-radius:3px}
  .sort-select svg{position:absolute;right:6px;top:3px}
  .results-rule{position:absolute;left:234px;top:230px;width:514px;height:2px;background:var(--line)}

  .map{position:absolute;left:48px;top:239px;width:168px;height:128px;background:linear-gradient(115deg,#ececec 0%,#ececec 45%,var(--map-sea) 60%,var(--map-sea) 100%)}

  /* filter */
  .filter{position:absolute;left:48px;top:386px;width:168px;height:418px;background:var(--white);border-radius:3px;box-shadow:0 1px 3px rgba(0,0,0,.05)}
  .filter h3{position:absolute;font-family:'Montserrat',sans-serif;font-weight:400;font-size:11px;color:#333}
  .filter-search{position:absolute;left:14px;top:44px;width:131px;height:17px;border:1.5px solid #e1e4e8;border-radius:4px;font-size:7px;color:#888;padding-left:12px;line-height:14px;font-family:'Montserrat',sans-serif}
  .filter-search svg{position:absolute;right:8px;top:3px}
  .price-range{position:absolute;left:16px;top:102px;font-size:6px;font-family:'Montserrat',sans-serif;color:#555}
  .slider{position:absolute;left:16px;top:115px;width:126px;height:1px;background:#ccc}
  .slider .fill{position:absolute;left:12px;width:104px;height:2px;top:-1px;background:var(--blue-bright)}
  .slider .knob{position:absolute;top:-4px;width:8px;height:8px;border:1px solid #bbb;border-radius:50%;background:var(--white)}
  .row{position:absolute;left:16px;width:130px;font-size:7px;font-family:'Montserrat',sans-serif;color:#333;height:10px;line-height:9px}
  .row .box{position:absolute;left:0;top:1px;width:7px;height:7px;border:1px solid #cfcfcf}
  .row .lbl{position:absolute;left:13px}
  .row .stars{position:absolute;left:42px;top:0}
  .row .count{position:absolute;right:0}

  /* cards */
  .card{position:absolute;left:234px;width:514px;height:126px;background:var(--white);box-shadow:0 1px 3px rgba(0,0,0,.05)}
  .card .photo{position:absolute;left:4px;top:6px;width:159px;height:112px;background:var(--blue-bright);border-radius:2px}
  .card h2{position:absolute;left:171px;top:8px;font-family:'Montserrat',sans-serif;font-weight:400;font-size:13.5px;color:var(--ink)}
  .card .meta{position:absolute;left:170px;top:34px;display:flex;align-items:center;gap:4px;font-size:7px;font-family:'Montserrat',sans-serif;color:#444}
  .card .amen{position:absolute;left:170px;top:56px}
  .card .score{position:absolute;left:170px;top:78px;display:flex;align-items:center;gap:3px;font-size:9px;font-family:'Raleway',sans-serif;color:#222}
  .score .badge{background:var(--green-badge);color:var(--white);font-size:8px;padding:3px 4px;border-radius:2px;font-weight:600}
  .score b{font-weight:600}
  .score span{color:#777}
  .card .booked{position:absolute;left:172px;top:106px;font-size:9.5px;font-family:'Montserrat',sans-serif;color:var(--green)}
  .card .price{position:absolute;right:8px;top:40px;font-family:'Raleway',sans-serif;font-weight:600;font-size:17px;color:var(--ink)}
  .card .per{position:absolute;right:8px;top:62px;font-size:8.5px;color:#777}
  .card .book{position:absolute;right:8px;top:80px;width:63px;height:24px;background:var(--blue-btn);color:var(--white);font-size:8.5px;text-align:center;line-height:24px;box-shadow:0 2px 4px rgba(0,0,0,.2)}

  .more-btn{position:absolute;left:368px;top:851px;width:94px;height:21px;background:var(--green);border-radius:2px;color:var(--white);font-family:'Montserrat',sans-serif;font-size:12px;text-align:center;line-height:21px}

  /* footer */
  .site-footer{position:absolute;left:0;top:925px;width:814px;height:275px;background:var(--blue-dark);border-top:4px solid var(--green);color:var(--white);font-family:'Roboto Condensed',sans-serif}
  .site-footer h4{position:absolute;font-weight:400;font-size:12.5px;letter-spacing:.2px}
  .site-footer ul{position:absolute;list-style:none;font-size:9px;line-height:19.4px}
  .news-input{position:absolute;left:478px;top:80px;width:160px;height:27px;background:var(--white);border:1.5px solid var(--green)}
  .news-btn{position:absolute;left:637px;top:80px;width:66px;height:27px;background:var(--green);font-size:11px;text-align:center;line-height:27px;font-family:'Raleway',sans-serif}
  .news-note{position:absolute;left:478px;top:120px;font-size:10.5px;font-family:'Montserrat',sans-serif;font-weight:400}
  .footer-rule{position:absolute;left:90px;top:218px;width:635px;height:1px;background:rgba(255,255,255,.35)}
  .copyright{position:absolute;left:0;top:239px;width:836px;text-align:center;font-size:10px}
</style>
</head>
<body>
<svg width="0" height="0" style="position:absolute">
  <defs>
    <symbol id="star" viewBox="0 0 10 10"><path d="M5 .4l1.4 3 3.2.3-2.4 2.1.7 3.2L5 7.3 2.1 9l.7-3.2L.4 3.7l3.2-.3z"/></symbol>
    <symbol id="pin" viewBox="0 0 10 12"><path d="M5 0a4 4 0 0 0-4 4c0 3 4 8 4 8s4-5 4-8a4 4 0 0 0-4-4zm0 5.6A1.6 1.6 0 1 1 5 2.4a1.6 1.6 0 0 1 0 3.2z"/></symbol>
    <symbol id="amenities" viewBox="0 0 130 12">
      <g fill="none" stroke="#666" stroke-width="1.2">
        <path d="M1 5a7 7 0 0 1 10 0M3 7.5a4 4 0 0 1 6 0"/><circle cx="6" cy="10" r=".8" fill="#666"/>
        <path d="M20 1v10M18 1v4h4V1M25 1c-2 2-2 5 0 5v5"/>
        <path d="M33 1h8l-4 5v5M34.5 11h5"/>
        <rect x="55" y="2" width="7" height="8"/>
        <path d="M73 3h8v6h-8zM70 11l4-4"/>
        <rect x="91" y="2" width="7" height="8"/>
        <path d="M108 6h10M109 3v6M111 1v10M115 1v10M117 3v6"/>
      </g>
    </symbol>
  </defs>
</svg>

<header class="site-header">
  <div class="brand"><span class="brand-mark"></span><span class="brand-name">IsleRoute</span></div>
  <nav class="top-nav"><span>Home</span><span>about</span><span>contact</span><span>Login</span><span>Signup</span></nav>
  <svg class="user-icon" width="19" height="21" viewBox="0 0 19 21" fill="#c4c7ca"><circle cx="9.5" cy="6" r="5"/><path d="M0 21c0-6 4-9 9.5-9S19 15 19 21z"/></svg>
</header>

<nav class="main-nav">
  <ul><li>Discover cayman</li><li>Thing to do</li><li>Hotels</li><li>Trip Planer</li><li>Map</li></ul>
</nav>

<div class="field" style="left:49px">Location
  <svg width="16" height="16" viewBox="0 0 16 16" fill="none" stroke="#bbb"><path d="M8 1a4 4 0 0 0-4 4c0 3 4 7 4 7s4-4 4-7a4 4 0 0 0-4-4z"/><path d="M1 15l3-4h8l3 4z"/></svg></div>
<div class="field" style="left:191px">Check in
  <svg width="16" height="16" viewBox="0 0 16 16" fill="none" stroke="#bbb"><rect x="1" y="2" width="14" height="13"/><path d="M1 6h14M4 9h2M7 9h2M10 9h2M4 12h2M7 12h2M10 12h2"/></svg></div>
<div class="field" style="left:333px">Check out
  <svg width="16" height="16" viewBox="0 0 16 16" fill="none" stroke="#bbb"><rect x="1" y="2" width="14" height="13"/><path d="M1 6h14M4 9h2M7 9h2M10 9h2M4 12h2M7 12h2M10 12h2"/></svg></div>
<div class="field" style="left:475px;padding-left:17px">Guests &amp; Rooms</div>
<div class="search-btn">Search</div>

<div class="results-bar">Cayman Island : 100 Results Found</div>
<div class="taxes">Taxs Included</div>
<div class="sort-label">Sort By :</div>
<div class="sort-select"><svg width="7" height="11" viewBox="0 0 7 11" fill="#999"><path d="M3.5 0L7 4H0zM3.5 11L0 7h7z"/></svg></div>
<div class="results-rule"></div>

<div class="map" role="img" aria-label="Map of the island coast with hotel locations marked"></div>

<aside class="filter">
  <h3 style="left:14px;top:20px">Filter</h3>
  <div class="filter-search">Search
    <svg width="8" height="8" viewBox="0 0 8 8" fill="none" stroke="#888"><circle cx="3.2" cy="3.2" r="2.5"/><path d="M5 5l2.5 2.5"/></svg></div>
  <h3 style="left:15px;top:84px">Price</h3>
  <div class="price-range">$100 to $1000</div>
  <div class="slider"><div class="fill"></div><div class="knob" style="left:8px"></div><div class="knob" style="left:112px"></div></div>
  <h3 style="left:16px;top:135px">Star Rating</h3>

  <div class="row" style="top:160px"><span class="box"></span><span class="lbl">5 Star</span>
    <svg class="stars" width="50" height="9"><use href="#star" x="0" width="8" height="8" fill="var(--star)"/><use href="#star" x="10" width="8" height="8" fill="var(--star)"/><use href="#star" x="20" width="8" height="8" fill="var(--star)"/><use href="#star" x="30" width="8" height="8" fill="var(--star)"/><use href="#star" x="40" width="8" height="8" fill="var(--star)"/></svg>
    <span class="count">300</span></div>
  <div class="row" style="top:178px"><span class="box"></span><span class="lbl">4 Star</span>
    <svg class="stars" width="50" height="9"><use href="#star" x="0" width="8" height="8" fill="var(--star)"/><use href="#star" x="10" width="8" height="8" fill="var(--star)"/><use href="#star" x="20" width="8" height="8" fill="var(--star)"/><use href="#star" x="30" width="8" height="8" fill="var(--star)"/><use href="#star" x="40" width="8" height="8" fill="var(--star-off)"/></svg>
    <span class="count">350</span></div>
  <div class="row" style="top:196px"><span class="box"></span><span class="lbl">3 Star</span>
    <svg class="stars" width="50" height="9"><use href="#star" x="0" width="8" height="8" fill="var(--star)"/><use href="#star" x="10" width="8" height="8" fill="var(--star)"/><use href="#star" x="20" width="8" height="8" fill="var(--star)"/><use href="#star" x="30" width="8" height="8" fill="var(--star-off)"/><use href="#star" x="40" width="8" height="8" fill="var(--star-off)"/></svg>
    <span class="count">250</span></div>
  <div class="row" style="top:214px"><span class="box"></span><span class="lbl">2 Star</span>
    <svg class="stars" width="50" height="9"><use href="#star" x="0" width="8" height="8" fill="var(--star)"/><use href="#star" x="10" width="8" height="8" fill="var(--star)"/><use href="#star" x="20" width="8" height="8" fill="var(--star-off)"/><use href="#star" x="30" width="8" height="8" fill="var(--star-off)"/><use href="#star" x="40" width="8" height="8" fill="var(--star-off)"/></svg>
    <span class="count">150</span></div>
  <div class="row" style="top:232px"><span class="box"></span><span class="lbl">1 Star</span>
    <svg class="stars" width="50" height="9"><use href="#star" x="0" width="8" height="8" fill="var(--star)"/><use href="#star" x="10" width="8" height="8" fill="var(--star-off)"/><use href="#star" x="20" width="8" height="8" fill="var(--star-off)"/><use href="#star" x="30" width="8" height="8" fill="var(--star-off)"/><use href="#star" x="40" width="8" height="8" fill="var(--star-off)"/></svg>
    <span class="count">170</span></div>

  <h3 style="left:16px;top:269px">Poperty Type</h3>
  <div class="row" style="top:297px"><span class="box"></span><span class="lbl" style="left:15px">Hotel</span><span class="count">250</span></div>
  <div class="row" style="top:317px"><span class="box"></span><span class="lbl" style="left:15px">Resort</span><span class="count">250</span></div>
  <div class="row" style="top:338px"><span class="box"></span><span class="lbl" style="left:15px">Motel</span><span class="count">250</span></div>
  <div class="row" style="top:358px"><span class="box"></span><span class="lbl" style="left:15px">Guest House</span><span class="count">250</span></div>
  <div class="row" style="top:379px"><span class="box"></span><span class="lbl" style="left:15px">Island</span><span class="count">250</span></div>
</aside>

<article class="card" style="top:241px">
  <div class="photo" role="img" aria-label="Hotel photo"></div>
  <h2>Hotel Booking</h2>
  <div class="meta"><svg width="48" height="10"><use href="#star" x="0" width="10" height="10" fill="var(--star)"/><use href="#star" x="12" width="10" height="10" fill="var(--star)"/><use href="#star" x="24" width="10" height="10" fill="var(--star)"/><use href="#star" x="36" width="10" height="10" fill="var(--star)"/></svg><svg width="8" height="9" fill="#555"><use href="#pin" width="8" height="9"/></svg>&nbsp;Location</div>
  <svg class="amen" width="130" height="12"><use href="#amenities"/></svg>
  <div class="score"><span class="badge">8.2</span><b>Excellent</b><span>(245 reviews)</span></div>
  <div class="booked">Last Booked - 1day ago</div>
  <div class="price">$210</div><div class="per">1 Room/Night</div><div class="book">Book Now</div>
</article>

<article class="card" style="top:385px">
  <div class="photo" role="img" aria-label="Hotel photo"></div>
  <h2>Hotel Booking</h2>
  <div class="meta"><svg width="60" height="10"><use href="#star" x="0" width="10" height="10" fill="var(--star)"/><use href="#star" x="12" width="10" height="10" fill="var(--star)"/><use href="#star" x="24" width="10" height="10" fill="var(--star)"/><use href="#star" x="36" width="10" height="10" fill="var(--star)"/><use href="#star" x="48" width="10" height="10" fill="var(--star)"/></svg><svg width="8" height="9" fill="#555"><use href="#pin" width="8" height="9"/></svg>&nbsp;Location</div>
  <svg class="amen" width="130" height="12"><use href="#amenities"/></svg>
  <div class="score"><span class="badge">7.0</span><b>Good</b><span>(420 reviews)</span></div>
  <div class="booked">Last Booked - 1day ago</div>
  <div class="price">$280</div><div class="per">1 Room/Night</div><div class="book">Book Now</div>
</article>

<article class="card" style="top:530px">
  <div class="photo" role="img" aria-label="Hotel photo" style="left:7px"></div>
  <h2>Hotel Booking</h2>
  <div class="meta"><svg width="60" height="10"><use href="#star" x="0" width="10" height="10" fill="var(--star)"/><use href="#star" x="12" width="10" height="10" fill="var(--star)"/><use href="#star" x="24" width="10" height="10" fill="var(--star)"/><use href="#star" x="36" width="10" height="10" fill="var(--star)"/><use href="#star" x="48" width="10" height="10" fill="var(--star)"/></svg><svg width="8" height="9" fill="#555"><use href="#pin" width="8" height="9"/></svg>&nbsp;Location</div>
  <svg class="amen" width="130" height="12"><use href="#amenities"/></svg>
  <div class="score"><span class="badge">9.6</span><b>Excellent</b><span>(1206 reviews)</span></div>
  <div class="booked">Last Booked - 1day ago</div>
  <div class="price">$675</div><div class="per">1 Room/Night</div><div class="book">Book Now</div>
</article>

<article class="card" style="top:679px">
  <div class="photo" role="img" aria-label="Hotel photo" style="left:9px"></div>
  <h2>Hotel Booking</h2>
  <div class="meta"><svg width="48" height="10"><use href="#star" x="0" width="10" height="10" fill="var(--star)"/><use href="#star" x="12" width="10" height="10" fill="var(--star)"/><use href="#star" x="24" width="10" height="10" fill="var(--star)"/><use href="#star" x="36" width="10" height="10" fill="var(--star)"/></svg><svg width="8" height="9" fill="#555"><use href="#pin" width="8" height="9"/></svg>&nbsp;Location</div>
  <svg class="amen" width="130" height="12"><use href="#amenities"/></svg>
  <div class="score"><span class="badge">8.2</span><b>Excellent</b><span>(245 reviews)</span></div>
  <div class="booked">Last Booked - 1day ago</div>
  <div class="price">$210</div><div class="per">1 Room/Night</div><div class="book">Book Now</div>
</article>

<div class="more-btn">More</div>

<footer class="site-footer">
  <h4 style="left:98px;top:47px">COMPANY</h4>
  <ul style="left:98px;top:80px"><li>About us</li><li>How it works ?</li><li>Our investors</li><li>Contact us</li><li>Work with us</li></ul>
  <h4 style="left:211px;top:49px">SUPPORT</h4>
  <ul style="left:211px;top:80px"><li>FAQ</li><li>Legal notices</li><li>Cancellation policy</li><li>Terms of use</li><li>Privacy policy</li></ul>
  <h4 style="left:344px;top:48px">QUICK LINKS</h4>
  <ul style="left:345px;top:81px"><li>Discover Cayman</li><li>Thing to Do</li><li>My Trip Planner</li><li>Map</li><li>Contact Us</li></ul>
  <h4 style="left:478px;top:57px;font-size:11px">SIGN UP IN NEWSLETTER</h4>
  <div class="news-input"></div>
  <div class="news-btn">Signup</div>
  <div class="news-note">Keep up to date as we expand in to new regions</div>
  <div class="footer-rule"></div>
  <div class="copyright">Copyright © 2019, IsleRoute. All rights reserved &nbsp;| &nbsp;Privacy policy &nbsp;| &nbsp;Terms and conditions</div>
</footer>
</body>
</html>
```